New modern business card design

To design a brand new business card that's clean & modern in terms of layout.
I have attached our company logo and also basic information regarding what is needed on the card that also needs to be editable.

Target Market(s)

motor trade

Contact Information for Business Card

logo, name, title, tel, mob, email, address, www, all information is in the word.doc file

Requirements
Must have
• white background
Nice to have
• Nice clean font

```html
<!DOCTYPE html>
<html lang="en">
<head>
<meta charset="utf-8">
<title>Torque Lift Ltd – Business Card</title>
<link href="https://fonts.googleapis.com/css2?family=Montserrat:wght@500;600&family=Roboto:wght@400&display=swap" rel="stylesheet">
<style>
  :root {
    --stage: #5f5f5f;
    --brand-blue: #4472b8;
    --card-white: #ffffff;
    --ink: #333333;
  }
  * { margin: 0; padding: 0; box-sizing: border-box; }
  html, body { width: 1200px; height: 1200px; overflow: hidden; }
  body {
    background: var(--stage);
    position: relative;
    font-family: "Roboto", Arial, sans-serif;
  }
  .card {
    position: absolute;
    left: 228px;
    width: 744px;
    height: 425px;
    border-radius: 26px;
    overflow: hidden;
  }
  .card--front { top: 148px; background: var(--brand-blue); }
  .card--back { top: 640px; background: var(--card-white); }

  .brand {
    position: absolute;
    display: flex;
    align-items: center;
    font-family: "Montserrat", Arial, sans-serif;
    font-weight: 600;
    white-space: nowrap;
  }
  .brand__square { display: block; }
  .card--front .brand {
    left: 0; right: 0; top: 180px;
    justify-content: center;
    gap: 18px;
    font-size: 46px;
    color: var(--card-white);
  }
  .card--front .brand__square { width: 40px; height: 40px; background: var(--card-white); }
  .card--front .website {
    position: absolute;
    left: 0; right: 0; top: 376px;
    text-align: center;
    font-size: 16px;
    letter-spacing: 2.5px;
    color: var(--card-white);
  }

  .card--back .brand {
    right: 30px; top: 74px;
    gap: 12px;
    font-size: 30px;
    color: var(--brand-blue);
  }
  .card--back .brand__square { width: 26px; height: 26px; background: var(--brand-blue); }

  .person {
    position: absolute;
    left: 26px; top: 204px;
  }
  .person__name {
    font-family: "Montserrat", Arial, sans-serif;
    font-weight: 500;
    font-size: 27px;
    color: var(--brand-blue);
    line-height: 1;
  }
  .person__name strong { font-weight: 600; }
  .person__title {
    margin: 10px 0 0 28px;
    font-size: 17px;
    color: var(--ink);
  }

  .contacts {
    position: absolute;
    left: 26px; top: 276px;
    list-style: none;
  }
  .contacts li {
    display: flex;
    align-items: center;
    height: 24px;
    margin-bottom: 8px;
    font-size: 17px;
    color: var(--ink);
  }
  .contacts svg { width: 18px; height: 18px; margin-right: 11px; flex: none; }

  .address {
    position: absolute;
    left: 478px; top: 350px;
    display: flex;
    align-items: flex-start;
    font-size: 16px;
    line-height: 22px;
    color: var(--ink);
    font-style: normal;
  }
  .address svg { width: 16px; height: 20px; margin: 3px 10px 0 0; flex: none; }
</style>
</head>
<body>

<section class="card card--front" aria-label="Card front">
  <div class="brand"><span class="brand__square"></span>TORQUE LIFT LTD</div>
  <p class="website">www.torque-lift.co.uk</p>
</section>

<section class="card card--back" aria-label="Card back">
  <div class="brand"><span class="brand__square"></span>TORQUE LIFT LTD</div>

  <div class="person">
    <h1 class="person__name"><strong>DANIEL</strong> HARPER</h1>
    <p class="person__title">General Manager</p>
  </div>

  <ul class="contacts">
    <li>
      <svg viewBox="0 0 24 24" fill="none" stroke="#4472b8" stroke-width="2" stroke-linecap="round" stroke-linejoin="round"><path d="M5 3h4l2 5-2.5 1.5a11 11 0 0 0 6 6L16 13l5 2v4a2 2 0 0 1-2 2A16 16 0 0 1 3 5a2 2 0 0 1 2-2z"/><path d="M15 3a6 6 0 0 1 6 6M15 7a2 2 0 0 1 2 2"/></svg>
      0161 555 0142
    </li>
    <li>
      <svg viewBox="0 0 24 24" fill="none" stroke="#4472b8" stroke-width="2" stroke-linecap="round"><rect x="6" y="2" width="12" height="20" rx="2"/><path d="M11 18h2"/></svg>
      07700 900 318
    </li>
    <li>
      <svg viewBox="0 0 24 24" fill="none" stroke="#4472b8" stroke-width="2" stroke-linejoin="round"><rect x="2" y="5" width="20" height="14" rx="1"/><path d="M2 6l10 7 10-7"/></svg>
      dharper@torque-lift.co.uk
    </li>
    <li>
      <svg viewBox="0 0 24 24" fill="none" stroke="#4472b8" stroke-width="2"><circle cx="12" cy="12" r="10"/><path d="M2 12h20M12 2a15 15 0 0 1 0 20M12 2a15 15 0 0 0 0 20"/></svg>
      www.torque-lift.co.uk
    </li>
  </ul>

  <address class="address">
    <svg viewBox="0 0 16 20"><path fill="#4472b8" d="M8 0a7 7 0 0 0-7 7c0 5 7 13 7 13s7-8 7-13a7 7 0 0 0-7-7zm0 10a3 3 0 1 1 0-6 3 3 0 0 1 0 6z"/></svg>
    <span>Orchard Street, Bramhall<br>Manchester, M99 4QT</span>
  </address>
</section>

</body>
</html>
```